Web-Bannerlayouts für lokalen Radiosender
Zielgruppe
Funk Tessaro ist ein lokaler Radiosender für München und die Region. Funk Tessaro ist täglicher Begleiter der Zielgruppe (Hörer ab 30+) mit regionalen News, Verkehr, Wetter, Freizeit- und Veranstaltungstipps, Podcasts und EINFACH GUTER MUSIK.
Aufgabenstellung
Gestaltung neuer Web-Bannerlayouts zur Eigenpromotion der App - Webbanner werden auf der Funk Tessaro-Homepage eingesetzte. Template im Funk Tessaro-Stil - Inhalt (nach Bedarf) austauschbar.
Formate:
320 x 100
320 x 250
320 x 480
470 x 160 (Signatur Grafik)
920 x 250
970 x 90
Wichtig: Call-to-Action-Button ('Jetzt installieren' / 'Jetzt Download') / Funk Tessaro Logo / App Icon
CI-Farben: Magenta (R 229/ G 0/ B 125) und Blau (R 4/ G 64/ B 135)

```html
<!DOCTYPE html>
<html lang="de">
<head>
<meta charset="utf-8">
<title>Funk Tessaro – App-Banner</title>
<link href="https://fonts.googleapis.com/css2?family=Exo+2:wght@600;700&display=swap" rel="stylesheet">
<style>
  :root {
    --magenta: #e5007d;
    --magenta-deep: #c8006c;
    --blue: #044087;
    --white: #ffffff;
    --badge: #111111;
    --stage: #e6e6e6;
    --photo-a: #b3115f;
    --photo-b: #1b5f93;
    --photo-c: #29c6e6;
  }
  * { box-sizing: border-box; margin: 0; padding: 0; }
  html, body { width: 1200px; height: 784px; overflow: hidden; background: var(--stage); }
  body { position: relative; font-family: "Exo 2", Arial, sans-serif; }

  .banner { position: absolute; background: var(--magenta); overflow: hidden; }
  .photo {
    position: absolute;
    background: linear-gradient(120deg, var(--photo-a) 0%, var(--photo-b) 45%, var(--photo-c) 80%, var(--photo-a) 100%);
  }
  .headline {
    position: absolute; color: var(--white); font-weight: 700;
    line-height: 1.12; white-space: nowrap; letter-spacing: 0.2px;
  }
  .cta {
    position: absolute; background: var(--blue); color: var(--white);
    font-weight: 700; border-radius: 999px;
    display: flex; align-items: center; justify-content: center; white-space: nowrap;
  }
  .store-badge {
    position: absolute; background: var(--badge);
    border: 1px solid #8a8a8a; border-radius: 3px;
  }

  .app-icon {
    position: absolute; border-radius: 1.6em; overflow: hidden;
    background: var(--magenta-deep); box-shadow: 0 0.2em 0.6em rgba(0,0,0,0.25);
  }
  .app-icon .icon-top {
    position: absolute; left: 0; top: 0; width: 100%; height: 58%;
    background: var(--white); display: flex; align-items: center; justify-content: center;
    text-align: center;
  }
  .app-icon .icon-name {
    color: var(--blue); font-weight: 700; font-size: 1.55em; line-height: 0.95;
  }
  .app-icon svg { position: absolute; left: 50%; top: 79%; width: 3.4em; height: 3.4em; transform: translate(-50%, -50%); }

  /* Hochformat */
  .banner-portrait { left: 55px; top: 209px; width: 295px; height: 443px; }
  .banner-portrait .photo { left: 0; top: 198px; width: 295px; height: 245px; }
  .banner-portrait .headline { left: 19px; top: 30px; font-size: 24.5px; }
  .banner-portrait .cta { left: 20px; top: 99px; width: 200px; height: 35px; font-size: 15px; }

  /* Mittleres Querformat */
  .banner-medium { left: 381px; top: 130px; width: 651px; height: 222px; }
  .banner-medium .photo { left: 0; top: 0; width: 254px; height: 222px; }
  .banner-medium .headline { left: 284px; top: 22px; font-size: 32.5px; }
  .banner-medium .cta { left: 389px; top: 115px; width: 234px; height: 41px; font-size: 18px; }

  /* Breites Querformat */
  .banner-wide { left: 381px; top: 382px; width: 764px; height: 166px; }
  .banner-wide .photo { left: 0; top: 0; width: 313px; height: 166px; }
  .banner-wide .headline { left: 412px; top: 22px; font-size: 29px; }
  .banner-wide .cta { left: 412px; top: 102px; width: 210px; height: 37px; font-size: 16px; }

  /* Leaderboard */
  .banner-strip { left: 381px; top: 578px; width: 764px; height: 74px; }
  .banner-strip .photo { left: 0; top: 0; width: 240px; height: 74px;
    -webkit-mask-image: linear-gradient(90deg, #000 75%, transparent); mask-image: linear-gradient(90deg, #000 75%, transparent); }
  .banner-strip .headline { left: 301px; top: 10px; font-size: 22px; }
  .banner-strip .cta { left: 579px; top: 12px; width: 154px; height: 28px; font-size: 12px; }
</style>
</head>
<body>

<!-- Hochformat 320 x 480 -->
<section class="banner banner-portrait">
  <div class="photo" role="img" aria-label="Foto: lachende Frau mit Kopfhörern und Sonnenbrille in Magenta- und Cyanlicht"></div>
  <h2 class="headline">Das volle Programm –<br>auch auf Ihrem Handy!</h2>
  <a class="cta">Jetzt App downloaden!</a>
  <span class="store-badge" style="left:24px;top:151px;width:67px;height:22px" aria-label="Store-Badge"></span>
  <span class="store-badge" style="left:95px;top:151px;width:75px;height:22px" aria-label="Store-Badge"></span>
  <div class="app-icon" style="left:187px;top:151px;width:89px;height:88px;font-size:8.9px">
    <div class="icon-top"><span class="icon-name">Funk<br>Tessaro</span></div>
    <svg viewBox="0 0 34 34" aria-hidden="true"><circle cx="17" cy="17" r="14.5" fill="none" stroke="#fff" stroke-width="2.6"/><path d="M13 10 L24 17 L13 24 Z" fill="#fff"/></svg>
  </div>
</section>

<!-- Querformat 920 x 250 -->
<section class="banner banner-medium">
  <div class="photo" role="img" aria-label="Foto: lachende Frau mit Kopfhörern und Sonnenbrille in Magenta- und Cyanlicht"></div>
  <h2 class="headline">Das volle Programm –<br>auch auf Ihrem Handy!</h2>
  <div class="app-icon" style="left:283px;top:130px;width:92px;height:92px;font-size:9.2px">
    <div class="icon-top"><span class="icon-name">Funk<br>Tessaro</span></div>
    <svg viewBox="0 0 34 34" aria-hidden="true"><circle cx="17" cy="17" r="14.5" fill="none" stroke="#fff" stroke-width="2.6"/><path d="M13 10 L24 17 L13 24 Z" fill="#fff"/></svg>
  </div>
  <a class="cta">Jetzt App downloaden!</a>
  <span class="store-badge" style="left:389px;top:174px;width:86px;height:28px" aria-label="Store-Badge"></span>
  <span class="store-badge" style="left:482px;top:174px;width:91px;height:28px" aria-label="Store-Badge"></span>
</section>

<!-- Breites Format -->
<section class="banner banner-wide">
  <div class="photo" role="img" aria-label="Foto: lachende Frau mit Kopfhörern und Sonnenbrille in Magenta- und Cyanlicht"></div>
  <div class="app-icon" style="left:272px;top:24px;width:118px;height:117px;font-size:11.8px">
    <div class="icon-top"><span class="icon-name">Funk<br>Tessaro</span></div>
    <svg viewBox="0 0 34 34" aria-hidden="true"><circle cx="17" cy="17" r="14.5" fill="none" stroke="#fff" stroke-width="2.6"/><path d="M13 10 L24 17 L13 24 Z" fill="#fff"/></svg>
  </div>
  <h2 class="headline">Das volle Programm –<br>auch auf Ihrem Handy!</h2>
  <a class="cta">Jetzt App downloaden!</a>
  <span class="store-badge" style="left:642px;top:102px;width:62px;height:20px" aria-label="Store-Badge"></span>
  <span class="store-badge" style="left:642px;top:126px;width:73px;height:22px" aria-label="Store-Badge"></span>
</section>

<!-- Leaderboard 970 x 90 -->
<section class="banner banner-strip">
  <div class="photo" role="img" aria-label="Foto: lachende Frau mit Kopfhörern und Sonnenbrille in Magenta- und Cyanlicht"></div>
  <div class="app-icon" style="left:221px;top:9px;width:59px;height:58px;font-size:5.9px">
    <div class="icon-top"><span class="icon-name">Funk<br>Tessaro</span></div>
    <svg viewBox="0 0 34 34" aria-hidden="true"><circle cx="17" cy="17" r="14.5" fill="none" stroke="#fff" stroke-width="2.6"/><path d="M13 10 L24 17 L13 24 Z" fill="#fff"/></svg>
  </div>
  <h2 class="headline">Das volle Programm –<br>auch auf Ihrem Handy!</h2>
  <a class="cta">Jetzt App downloaden!</a>
  <span class="store-badge" style="left:583px;top:46px;width:51px;height:18px" aria-label="Store-Badge"></span>
  <span class="store-badge" style="left:638px;top:46px;width:57px;height:18px" aria-label="Store-Badge"></span>
</section>

</body>
</html>
```